Logo and *CLEAR* creative Business Card

Looking for a creative transparent business card design for a custom clothing printing business for Businesses, Bands and Sportsteams; we will also be selling other promotional items, but our main focus is on t-shirts. The business name is Larkfield Apparel, and we are looking for something to make us stand out.

Will need a logo included. Must be easy to read, include a T-shirt somewhere in the logo or business card design, since that is our main focus, and we want that to be very clear. Logo should look good as a standalone logo, if the t-shirt were to be removed later, so the text is important.

Card should be credit card sized (slightly different than standard paper business cards): 85.5mm x 54mm. Needs 1.5mm bleed around edges.

Can be clear or frosted.

AI Vector file is best, or high quality 600+ dpi file.
Will require separate file of the logo, which should be large, or scalable.

Looking for something bold and modern. Hopefully something creative, and outside the box. Please see Look and Feel sliders.

We want the shape of a t-shirt, but it could be made to look metallic, glossy like shiny glass or plastic, a mosiac, or globs/brushes/splatter of paint. Each side of the shirt could be a different color if you want... We just want something that doesn't look like clip art of a typical t-shirt.
Updates

In case you missed it, I have changed the sliders, as well as a few details in the ad.  I have also added new pictures of examples for inspiration. 

One thing that is important to note, is the QR barcode, should not be transparent, since I worry that people will try to scan it from the wrong side, or it will be hard to scan depending on what is behind the card.

Please do not simply copy a logo from the attached files.  They are for inspiration only, and would need to at least be altered before being used. 

I like the idea of making a t-shirt prominent in the business card design, maybe working it into the background, or into certain elements within it.

Thanks,

Dale.

 

Feel Free to do something unconventional and creative, playing with shapes or negative space within the layout.  Darker designs might work, as well as text with depth/shine/3d look.

**Please notice I have increased the budget of this project to make it worth the while of artists to raise the quality of the designs. 

I have updated the attached files, and included comments and suggestions for various ideas that could be used in business card designs. 

Included in these files, is a picture of hole punch options, which can be included in your designs.  It allows for a regular round hole punch, as well as an irregular longer version. 

Please also note that corners can be round or square. 

If you follow the recommendations, I'm sure you will end up with a good looking design.

Thanks,

Dale.

Reason: I feel like some designers need a little more time and then i can decide on fully developed designs.

Reason: Just looking for some requested alterations from my top choices

Target Market(s)

Would like to appeal to a wide variety of people: Business owners/managers, Sports teams, and Bands are our customers (in order of importance).

Industry/Entity Type

Credit Card

Requirements
Must have
• **T-shirt in design or logo or both**
- Modern
- Wide Appeal (appeal to educated 25 - 50 year olds)
- A QR barcode to scan to add contact info to someone's phone(we will supply barcode) with brief explanation of the barcode ("Add contact info: [%]")Barcode should not be over transparent background, which may make it difficult to scan, or could be scanned from the wrong side of the card.
- Name: Dale Wexcott
- Position: Owner
- Business Name: Larkfield Apparel
- Ph: (supplied on completion)
- e-mail address: ""
- facebook page:""

**Will not include an address or fax number**

-Under the Name, it should say "Custom T-Shirts, etc" or "T-Shirt Printing, etc."

Nice to have
• Since the business card is either clear or frosted transparent, I would like the amount of words that can be seen (backwards) from the otherside, kept to a minimum.

- A subtle amount of foil print would be nice.

- Would like to see examples that are CREATIVE, possibly involving the tshirt, so right away someone knows what the company is all about.

Can also include a slogan such as "Your Brand is Our Business"

Design Detail is appreciated! :) Possibly something unconventional.

-Hole punch somewhere in the design. See attached file.
Should not have
• - comic sans, or other over used/cliche fonts.

- Should not be too hard to read.

-

```html
<!DOCTYPE html>
<html lang="en">
<head>
<meta charset="utf-8">
<title>Larkfield Apparel – Business Card</title>
<link rel="stylesheet" href="https://fonts.googleapis.com/css2?family=Orbitron:wght@600;700&family=Arimo:wght@400&display=swap">
<style>
  :root {
    --backdrop: #d8d4ce;
    --card-frost: #efe9e0;
    --card-edge: #ddd4c7;
    --hole: #d2c9bc;
    --brand-blue: #3d68a6;
    --tag-red: #8c3a2c;
    --name-band: #6b86ab;
    --contact-band: #8e4538;
    --band-text: #ffffff;
    --shirt-light: #5a7fb8;
    --shirt-dark: #2f4e80;
  }
  html, body {
    margin: 0;
    padding: 0;
    width: 1200px;
    height: 793px;
    overflow: hidden;
    background: var(--backdrop);
  }
  .canvas {
    position: relative;
    width: 1200px;
    height: 793px;
  }
  .card {
    position: absolute;
    left: 100px;
    top: 89px;
    width: 997px;
    height: 611px;
    border-radius: 44px;
    background: var(--card-frost);
    box-shadow: inset 0 0 0 2px var(--card-edge);
  }
  .hole-punch {
    position: absolute;
    left: 53px;
    top: 43px;
    width: 72px;
    height: 72px;
    border-radius: 50%;
    background: var(--hole);
    box-shadow: inset 0 0 0 2px var(--card-edge);
  }
  .shirt-art {
    position: absolute;
    left: 155px;
    top: 133px;
    width: 187px;
    height: 165px;
  }
  .brand-name {
    position: absolute;
    left: 369px;
    top: 128px;
    margin: 0;
    font-family: 'Orbitron', sans-serif;
    font-weight: 700;
    font-size: 47px;
    line-height: 70px;
    letter-spacing: 1px;
    color: var(--brand-blue);
    text-transform: uppercase;
  }
  .brand-tagline {
    position: absolute;
    left: 370px;
    top: 274px;
    margin: 0;
    font-family: 'Orbitron', sans-serif;
    font-weight: 600;
    font-size: 19.5px;
    line-height: 28px;
    letter-spacing: 0.5px;
    color: var(--tag-red);
    text-transform: uppercase;
  }
  .name-block {
    position: absolute;
    left: 369px;
    top: 328px;
    width: 353px;
    height: 81px;
    background: var(--name-band);
    color: var(--band-text);
    font-family: 'Arimo', sans-serif;
    box-sizing: border-box;
    padding: 6px 0 0 12px;
  }
  .person-name {
    margin: 0;
    font-size: 41px;
    line-height: 44px;
  }
  .person-role {
    margin: 0;
    font-size: 24px;
    line-height: 26px;
  }
  .contact-list {
    position: absolute;
    left: 369px;
    top: 419px;
    width: 599px;
    margin: 0;
    padding: 0;
    list-style: none;
  }
  .contact-item {
    height: 36px;
    margin-bottom: 9px;
    padding-left: 10px;
    background: var(--contact-band);
    color: var(--band-text);
    font-family: 'Arimo', sans-serif;
    font-size: 24px;
    line-height: 36px;
  }
</style>
</head>
<body>
<div class="canvas">
  <div class="card">
    <div class="hole-punch"></div>

    <svg class="shirt-art" viewBox="0 0 187 165" role="img" aria-label="Faceted blue T-shirt illustration">
      <defs>
        <linearGradient id="shirtTone" x1="0" y1="0" x2="1" y2="1">
          <stop offset="0" stop-color="var(--shirt-light)"/>
          <stop offset="1" stop-color="var(--shirt-dark)"/>
        </linearGradient>
      </defs>
      <rect x="0" y="0" width="187" height="165" fill="url(#shirtTone)"/>
    </svg>

    <h1 class="brand-name">Larkfield<br>Apparel</h1>
    <p class="brand-tagline">Custom T-Shirt Printing</p>

    <div class="name-block">
      <p class="person-name">Dale Wexcott</p>
      <p class="person-role">Owner</p>
    </div>

    <ul class="contact-list">
      <li class="contact-item">xxx-xxx-xxxx</li>
      <li class="contact-item">hello@larkfieldapparel.com</li>
      <li class="contact-item">www.larkfieldapparel.com/community</li>
    </ul>
  </div>
</div>
</body>
</html>
```